Lead Sales Portal Needs to Generate B2B Signup's

We are looking for banner ad designs to drive new business (B2B) traffic to our insurance and mortgage industry self serve lead sites. The sites are HomeLoanProspectHub.com and CoverageProspectHub.com, and we service over 45,000 insurance agents and mortgage lenders in a self serve lead portal model. We want our banners to generate more of these clients.

Our clients come to our sites, browse our database and then pick out and purchase the consumer leads that they need to generate new business.

We advertise extensively on Zorvix and on other PPC platforms, and our existing banners are looking really tired.

Some of the ad copy that works well for us is:

Cherry Pick Your Life Leads - Why Pay More Than $3.50 For Life Insurance Leads?
Sign up today and we'll match up to $250

Agents - Here's $250 For New Clients. Cherry Pick Your Life Insurance Leads & Save! Sign up today and we'll match up to $250

One of our Landing Pages that performs well is here:
http://www.coverageprospecthub.com/lp/008/

One of our competitors ad's are here:

http://www.tralvo.com/search/results?q=PolicyBeacon&ad=427360

We're looking for a design that is eye catching, uses our "Deeply Discounted Leads" and our "$250 match bonus"

This is the second contest that we have for the same sites. The previous designs were great and really performed well, so we are looking for new designs now that 6 months have passed. I have uploaded some winning banners from the last group for your information.
Updates

Project Deadline Extended
Reason: I've been asked by some of the designers to delay a day to get their designs in. I'm happy to do it!

Target Market(s)

These are insurance agents and mortgage lenders. All of our clients are business' or individuals within the business. This is a B2B campaign, so we need something that is professional and upscale. These are NOT consumer facing ad's!

Industry/Entity Type

Insurance

Font styles to use
Sans Serif

Requirements
Must have
• We must have the logos for the sites in the banners. Also, we must have a call to action arrow and "Go" button. Some animation is necessary, (especially around the arrow and the GO button).

One or two designs.

File type

.JPEG
.JPG
.PNG
.GIF

File size

150 KB or smaller

Image sizes

Vertical rectangle: 240 x 400
Mobile leaderboard: 320 x 50
Banner: 468 x 60
Leaderboard: 728 x 90
Square: 250 x 250
Small square: 200 x 200
Large rectangle: 336 x 280
Inline rectangle: 300 x 250
Skyscraper: 120 x 600
Wide skyscraper: 160 x 600
Half-page: 300 x 600
Large leaderboard: 970 x 90

```html
<!DOCTYPE html>
<html lang="en">
<head>
<meta charset="utf-8">
<title>Coverage Prospect Hub – Vertical Banner</title>
<link rel="stylesheet" href="https://fonts.googleapis.com/css2?family=Roboto+Condensed:wght@400;700&family=Open+Sans:wght@400&display=swap">
<style>
  :root {
    --page-bg: #ecebe8;
    --panel-dark: #2a2a2a;
    --panel-darker: #1f1f1f;
    --leaf-green: #7fb80e;
    --leaf-green-dark: #4f8a06;
    --photo-sky: #e4eef4;
    --photo-tone: #b9cfe0;
    --headline-grey-top: #dcdcdc;
    --headline-grey-bottom: #b9b9b9;
    --headline-ink: #2b2b2b;
    --offer-grey-top: #8d8d8d;
    --offer-grey-bottom: #6b6b6b;
    --white: #ffffff;
  }
  * { box-sizing: border-box; margin: 0; padding: 0; }
  html, body {
    width: 1200px; height: 1189px; overflow: hidden;
    background: var(--page-bg);
  }
  .stage { position: relative; width: 1200px; height: 1189px; }
  .banner {
    position: absolute; left: 315px; top: 24px;
    width: 300px; height: 600px;
    transform: scale(1.9); transform-origin: 0 0;
    background: var(--panel-dark);
    overflow: hidden;
    box-shadow: 0 3px 8px rgba(0,0,0,.35);
    font-family: "Roboto Condensed", "Arial Narrow", sans-serif;
  }
  .brand-bar {
    position: absolute; left: 0; top: 0; width: 300px; height: 62px;
    background: linear-gradient(var(--panel-dark), var(--panel-darker));
    display: flex; align-items: center; justify-content: center; gap: 8px;
  }
  .brand-mark {
    width: 28px; height: 28px; border-radius: 50%;
    background: var(--white);
  }
  .brand-name {
    font-family: "Open Sans", Arial, sans-serif;
    font-size: 17px; color: var(--white); font-weight: 400;
  }
  .hero-photo {
    position: absolute; left: 0; top: 62px; width: 300px; height: 250px;
    background: radial-gradient(ellipse at 55% 60%, var(--photo-tone), var(--photo-sky) 70%);
  }
  .hero-curves { position: absolute; left: 0; top: 55px; width: 300px; height: 260px; }
  .headline-panel {
    position: absolute; left: 0; top: 312px; width: 300px; height: 90px;
    background: linear-gradient(var(--headline-grey-top), var(--headline-grey-bottom));
    border-bottom: 3px solid var(--leaf-green);
    display: flex; flex-direction: column; justify-content: center; align-items: center;
  }
  .headline {
    font-weight: 700; font-size: 20.5px; line-height: 27px; letter-spacing: .2px;
    color: var(--headline-ink); text-align: center; text-transform: uppercase;
    text-shadow: 0 1px 0 rgba(255,255,255,.6);
  }
  .benefit-list {
    position: absolute; left: 0; top: 405px; width: 300px; height: 105px;
    list-style: none; padding: 14px 0 0 33px;
    background: var(--panel-dark);
  }
  .benefit-list li {
    display: flex; align-items: center; gap: 10px;
    color: var(--white); font-size: 19px; line-height: 26px;
  }
  .benefit-list li::before {
    content: ""; width: 10px; height: 10px; border-radius: 50%;
    background: var(--white); flex: none;
  }
  .offer-panel {
    position: absolute; left: 0; top: 512px; width: 300px; height: 88px;
    background: linear-gradient(var(--offer-grey-top), var(--offer-grey-bottom));
  }
  .offer-text {
    position: absolute; left: 13px; top: 12px;
    color: var(--white); font-size: 19.5px; line-height: 29px;
    text-shadow: 0 1px 2px rgba(0,0,0,.4);
  }
  .offer-amount { font-weight: 700; font-size: 26px; }
  .cta-arrow { position: absolute; left: 228px; top: 14px; width: 56px; height: 30px; }
  .go-button {
    position: absolute; left: 209px; top: 44px; width: 82px; height: 32px;
    border-radius: 16px;
    background: linear-gradient(#4a4a4a, #1c1c1c);
    border: 1px solid #111;
    box-shadow: inset 0 1px 0 rgba(255,255,255,.25);
    display: flex; align-items: center; justify-content: space-between;
    padding: 0 8px 0 14px;
    color: var(--white); font-weight: 700; font-size: 19px;
  }
  .go-button svg { width: 24px; height: 22px; }
</style>
</head>
<body>
<main class="stage">
  <section class="banner">
    <header class="brand-bar">
      <span class="brand-mark"></span>
      <span class="brand-name">Coverage Prospect Hub</span>
    </header>

    <div class="hero-photo" role="img" aria-label="Photo of two smiling insurance professionals in business shirts standing with arms crossed"></div>
    <svg class="hero-curves" viewBox="0 0 300 260" aria-hidden="true">
      <path d="M0 30 Q150 -12 300 22 L300 7 L0 7 Z" fill="var(--panel-darker)"/>
      <path d="M0 30 Q150 -12 300 22 L300 40 Q150 8 0 48 Z" fill="var(--leaf-green)"/>
      <path d="M0 48 Q150 8 300 40 L300 44 Q150 14 0 52 Z" fill="var(--leaf-green-dark)"/>
      <path d="M0 238 Q150 205 300 240 L300 260 L0 260 Z" fill="var(--leaf-green)"/>
      <path d="M0 246 Q150 216 300 250 L300 260 L0 260 Z" fill="var(--leaf-green-dark)"/>
    </svg>

    <div class="headline-panel">
      <h1 class="headline">Why pay more than $3.50<br>for life insurance leads?</h1>
    </div>

    <ul class="benefit-list">
      <li>Chery Pick Your Leads</li>
      <li>No Minimums</li>
      <li>Deeply Discounted Leads</li>
    </ul>

    <div class="offer-panel">
      <p class="offer-text">Sign up today and we'll<br>match up to <span class="offer-amount">$250</span></p>
      <svg class="cta-arrow" viewBox="0 0 56 30" aria-hidden="true">
        <path d="M4 8 Q36 2 48 24" fill="none" stroke="var(--white)" stroke-width="2"/>
        <path d="M41 21 L49 27 L51 17" fill="none" stroke="var(--white)" stroke-width="2"/>
      </svg>
      <a class="go-button">GO
        <svg viewBox="0 0 24 22" aria-hidden="true">
          <path d="M1 7 H12 V1 L23 11 L12 21 V15 H1 Z" fill="var(--leaf-green)" stroke="#3d6e05" stroke-width="1"/>
        </svg>
      </a>
    </div>
  </section>
</main>
</body>
</html>
```